New Locksmith Business needs a newspaper ad

We need an ad for a new locksmith business in Colorado called Riverbend Key Co. Our service area is located near several world-class ski resorts, which fuel the local economy. We are a comprehensive locksmith business offering automotive, commercial and residential services. We provide modern, tech-savvy digital security solutions for your home or business.

Size of ad: 3.22" x 3.44" | PDF needed for final artwork file

Target Market(s)

Local residents, businesses, hotels and resorts. As well as visitors to the area that may need emergency lock out services. High income, high net worth clients.

Industry/Entity Type

Locksmith

Font styles to use
Sans Serif

Requirements
Must have
• *Include: Logo
*Include: 970.318.2957
*Include: riverbendkeyco.example
*Include photo of Gus, he's the locksmith
*Include text: New Business!
*Include text: Auto | Residential | Commercial
*Include: Innovative Locksmith Solutions
*Colors from the logo are the main colors to use; accent color is Chrome Yellow (#ffac00)
*Bank Gothic is the headline font and we like to use Oswald font for all other text
Nice to have
• It would be nice to include another photo, in addition to the photo of Gus, if there is space. I know it is a small space, so no worries if adding another photo will not work.

```html
<!DOCTYPE html>
<html lang="en">
<head>
<meta charset="utf-8">
<title>Riverbend Key Co – New Business Ad</title>
<link href="https://fonts.googleapis.com/css2?family=Michroma&family=Oswald:wght@400;500;600&display=swap" rel="stylesheet">
<style>
  :root {
    --brand-blue: #1e73be;
    --band-blue: #2b6ea6;
    --chrome-yellow: #ffac00;
    --ink: #3a3a3a;
    --page: #e8e8e8;
    --paper: #ffffff;
    --ad-shadow: #c9c9c9;
  }
  * { margin: 0; padding: 0; box-sizing: border-box; }
  html, body { width: 739px; height: 1200px; overflow: hidden; background: var(--page); }
  .stage { position: relative; width: 739px; height: 1200px; }
  .ad-shadow {
    position: absolute; left: 6px; top: 238px;
    width: 690px; height: 737px; background: var(--ad-shadow);
  }
  .ad {
    position: absolute; left: 24px; top: 222px;
    width: 966px; height: 1032px;
    transform: scale(0.7143); transform-origin: 0 0;
    background: var(--paper); overflow: hidden;
    font-family: "Oswald", sans-serif;
  }
  .brand {
    position: absolute; top: 38px; left: 0; width: 100%;
    display: flex; justify-content: center; align-items: center; gap: 22px;
  }
  .brand-dot { width: 58px; height: 58px; border-radius: 50%; background: var(--brand-blue); }
  .brand-name {
    font-family: "Oswald", sans-serif; font-weight: 500; font-size: 56px;
    letter-spacing: 3px; color: var(--brand-blue); text-transform: uppercase;
  }
  .hero-photo {
    position: absolute; left: 0; top: 174px; width: 966px; height: 300px;
    background: linear-gradient(180deg, #8fb7e0 0%, #c7d9ea 22%, #6f7f86 38%, #4f6b52 60%, #5d8a3e 100%);
  }
  .headline-band {
    position: absolute; left: 0; top: 432px; width: 966px; height: 140px;
    background: linear-gradient(180deg, rgba(36,104,164,0.92), rgba(43,110,166,0.97));
  }
  .headline {
    position: absolute; left: 0; top: 458px; width: 966px; text-align: center;
    font-family: "Michroma", sans-serif; font-size: 56px; letter-spacing: 6px;
    color: #fff; line-height: 1; font-weight: 400;
  }
  .services-tag {
    position: absolute; left: 263px; top: 540px; width: 440px; height: 46px;
    background: var(--chrome-yellow); color: var(--ink);
    font-weight: 500; font-size: 29px; line-height: 46px; text-align: center;
  }
  .service-photo { position: absolute; top: 610px; width: 269px; height: 186px; }
  .service-photo.key-handover { left: 55px; background: linear-gradient(135deg, #d9b79c, #7a6e63); }
  .service-photo.smart-lock { left: 365px; background: linear-gradient(90deg, #b7c98a 0%, #a9693b 25%, #8b5530 100%); }
  .service-photo.card-access { left: 651px; background: linear-gradient(90deg, #2e2623, #6b5447 55%, #3a3431); }
  .tagline {
    position: absolute; left: 181px; top: 820px; width: 604px;
    font-weight: 500; font-size: 41px; color: var(--ink); letter-spacing: 0;
    white-space: nowrap; text-align: center;
  }
  .footer-bands { position: absolute; left: 0; top: 0; width: 966px; height: 1032px; }
  .contact {
    position: absolute; left: 55px; color: #fff; font-weight: 500; font-size: 26px;
    display: flex; align-items: center; gap: 12px; white-space: nowrap; line-height: 1.2;
  }
  .contact.phone { top: 934px; }
  .contact.web { top: 972px; }
  .contact svg { width: 24px; height: 24px; flex: none; }
  .locksmith-name {
    position: absolute; left: 476px; top: 960px;
    font-weight: 500; font-size: 38px; color: var(--ink); white-space: nowrap;
  }
  .locksmith-photo {
    position: absolute; left: 810px; top: 745px; width: 156px; height: 287px;
    border-radius: 70px 70px 0 0;
    background: linear-gradient(180deg, #c98f78 0%, #d7a48c 45%, #1f4fd1 70%, #1c46c0 100%);
  }
</style>
</head>
<body>
<div class="stage">
  <div class="ad-shadow"></div>
  <div class="ad">
    <div class="brand">
      <div class="brand-dot"></div>
      <div class="brand-name">Riverbend Key Co</div>
    </div>

    <div class="hero-photo" role="img" aria-label="Photo of Colorado mountain range with forested ski slopes under a blue sky"></div>
    <div class="headline-band"></div>
    <h1 class="headline">NEW BUSINESS!</h1>
    <div class="services-tag">AUTO | RESIDENTIAL | COMMERCIAL</div>

    <div class="service-photo key-handover" role="img" aria-label="Photo of a car key being handed over"></div>
    <div class="service-photo smart-lock" role="img" aria-label="Photo of a smartphone controlling a smart door lock"></div>
    <div class="service-photo card-access" role="img" aria-label="Photo of a hand holding a key card to an access reader"></div>

    <p class="tagline">INNOVATIVE LOCKSMITH SOLUTIONS</p>

    <svg class="footer-bands" viewBox="0 0 966 1032" aria-hidden="true">
      <polygon points="0,916 731,916 722,928 470,928 400,1032 0,1032" fill="#1e73be"/>
      <polygon points="482,940 966,940 966,1032 408,1032" fill="#ffac00"/>
    </svg>

    <div class="contact phone">
      <svg viewBox="0 0 24 24"><path fill="#fff" d="M6.6 10.8a15 15 0 0 0 6.6 6.6l2.2-2.2c.3-.3.7-.4 1-.2 1.1.4 2.3.6 3.6.6.6 0 1 .4 1 1V20c0 .6-.4 1-1 1C10.6 21 3 13.4 3 4c0-.6.4-1 1-1h3.5c.6 0 1 .4 1 1 0 1.3.2 2.5.6 3.6.1.3 0 .7-.2 1z"/></svg>
      <span>970.318.2957</span>
    </div>
    <div class="contact web">
      <svg viewBox="0 0 24 24" fill="none" stroke="#fff" stroke-width="2"><circle cx="12" cy="12" r="9"/><ellipse cx="12" cy="12" rx="4" ry="9"/><path d="M3 12h18M5 7h14M5 17h14"/></svg>
      <span>www.riverbendkeyco.example</span>
    </div>
    <div class="locksmith-name">GUS DORRAN, CRL</div>

    <div class="locksmith-photo" role="img" aria-label="Portrait photo of Gus, the locksmith, in a blue polo shirt"></div>
  </div>
</div>
</body>
</html>
```